KINDLEWAY: Social Media Post COVID-19 & Flu #1

- Create a similar design for a Social Media Post Image
- Attached, Logo, sample flu social media image.
- KINDLEWAY - must be included - in the colors provided (see attachment)
- Protect your community. Protect Your Elders. Stay Vaccinated. - must be include
-COVID-19 & Flu - will be stated somewhere
- image of mom and sons
-might include boarder
- inspiration at https://orvatrine.org/, and https://www.facebook.com/Orvatrine

```html
<!DOCTYPE html>
<html lang="en">
<head>
<meta charset="utf-8">
<title>KINDLEWAY – Flu &amp; COVID-19 Vaccination Campaign</title>
<link rel="stylesheet" href="https://fonts.googleapis.com/css2?family=Barlow+Condensed:wght@500;600&family=Barlow+Semi+Condensed:wght@600&family=Rubik:wght@800&display=swap">
<style>
  :root {
    --teal: #4a9fa8;
    --brick: #b0574f;
    --cream: #fdf1e3;
    --cream-deep: #f6e2d2;
    --band: rgba(255, 255, 255, 0.86);
    --frame-a: #5a9ea6;
    --frame-b: #c9c9c9;
    --frame-c: #a7615b;
  }
  * { margin: 0; padding: 0; box-sizing: border-box; }
  html, body { width: 1200px; height: 1200px; overflow: hidden; background: #ffffff; }

  .post {
    position: relative;
    width: 1200px;
    height: 1200px;
    overflow: hidden;
  }

  .border-pattern {
    position: absolute;
    inset: 0;
    background: linear-gradient(135deg, var(--frame-a) 0%, var(--frame-b) 35%, var(--frame-c) 50%, var(--frame-b) 65%, var(--frame-a) 100%);
  }

  .panel {
    position: absolute;
    left: 37px; top: 37px;
    width: 1126px; height: 1126px;
    background: linear-gradient(180deg, var(--cream) 0%, var(--cream-deep) 100%);
    overflow: hidden;
  }

  .family-photo {
    position: absolute;
    left: 88px; top: 253px;
    width: 920px; height: 800px;
    border-radius: 260px 260px 0 0;
    background: radial-gradient(ellipse at 50% 30%, #b98a72 0%, #8a3b34 35%, #3a2a2a 70%, #6d4a52 100%);
  }
  .blanket {
    position: absolute;
    left: 0; top: 1050px;
    width: 1126px; height: 76px;
    background: linear-gradient(90deg, #3d3b48, #8a3f3c, #4b8f96, #3d3b48, #9a4a44);
  }

  .title-box {
    position: absolute;
    left: 42px; top: 42px;
    width: 746px; height: 204px;
    border: 6px solid var(--brick);
  }
  .title-word {
    position: absolute;
    left: 0; right: 0; top: 2px;
    text-align: center;
    font-family: "Barlow Condensed", sans-serif;
    font-weight: 500;
    font-size: 176px;
    line-height: 1;
    letter-spacing: 2px;
    color: var(--teal);
  }
  .campaign-tag {
    position: absolute;
    left: 88px; top: 217px;
    width: 648px; height: 50px;
    background: var(--brick);
    color: var(--cream);
    font-family: "Barlow Semi Condensed", sans-serif;
    font-weight: 600;
    font-size: 31px;
    line-height: 50px;
    text-align: center;
    letter-spacing: 1px;
  }

  .org-name {
    position: absolute;
    left: 846px; top: 120px;
    display: flex;
    align-items: center;
    gap: 12px;
    font-family: "Barlow Condensed", sans-serif;
    font-weight: 600;
    font-size: 50px;
    line-height: 1;
    letter-spacing: 1px;
    color: var(--teal);
  }
  .org-name .dot {
    width: 22px; height: 22px;
    border-radius: 50%;
    background: var(--brick);
  }

  .message-band {
    position: absolute;
    left: 0;
    width: 1126px;
    background: var(--band);
    box-shadow: 0 4px 6px rgba(0, 0, 0, 0.12);
    font-family: "Rubik", sans-serif;
    font-weight: 800;
    color: var(--teal);
    white-space: nowrap;
  }
  .message-band .accent { color: var(--brick); }
  .band-community { top: 621px; height: 109px; padding-left: 140px; font-size: 78px; line-height: 109px; }
  .band-elders    { top: 763px; height: 121px; padding-left: 135px; font-size: 90px; line-height: 121px; }
  .band-vaccinated{ top: 920px; height: 126px; padding-left: 134px; font-size: 118px; line-height: 126px; }
</style>
</head>
<body>
<main class="post">
  <div class="border-pattern" role="img" aria-label="Woven zigzag border pattern in teal, grey and brick red"></div>

  <section class="panel">
    <div class="family-photo" role="img" aria-label="Photo of a smiling mother embraced by her two sons, one in a red shirt and one in a black shirt"></div>
    <div class="blanket" role="img" aria-label="Patterned woven blanket the family sits on"></div>

    <header class="title-box">
      <h1 class="title-word">KINDLEWAY</h1>
    </header>
    <p class="campaign-tag">FLU &amp; COVID -19 VACCINATION CAMPAIGN</p>

    <div class="org-name"><span class="dot"></span>ORVATRINE</div>

    <p class="message-band band-community">Protect Your <span class="accent">Community</span></p>
    <p class="message-band band-elders">Protect Your <span class="accent">Elders</span></p>
    <p class="message-band band-vaccinated">Stay <span class="accent">Vaccinated</span></p>
  </section>
</main>
</body>
</html>
```